Maplerise Trading Inc. needs an innovative idea for letterhead and visiting cards.

Maplerise Trading Inc. is a Canadian brand since 2007. It is a renown dealer of kids and office furniture locally. Moreover, exporting electric fixtures e.g. switches, LED's, down-lights etc. to Middle East and Africa. We have initiated a number of steps including re-branding, to boost our export in 2020. We have successfully designed our new logo a few months ago through 'Artfolio' and now we are looking for an innovative idea for a letterhead.
Some key points:
• Red, black and white are the three colors used in all our packaging and furniture. (grey is optional)
• Shouldn’t be too wide.
• Use of watermark is preferable.
• You can visit our North American site at www.mapleriseinc.com. Export website of the company will be launched soon. www.mapleriseinc.ca
• Same letterhead will be used locally and internationally.
• Our new logo and sample packaging is attached.

```html
<!DOCTYPE html>
<html lang="en">
<head>
<meta charset="utf-8">
<title>Maplerise Trading Letterhead</title>
<link href="https://fonts.googleapis.com/css2?family=Roboto:wght@300;400&display=swap" rel="stylesheet">
<style>
  :root {
    --backdrop: #e2e2e2;
    --paper: #ffffff;
    --paper-shade: #f1f1f1;
    --brand-red: #a3171c;
    --ink-dark: #3f3f3f;
    --ink-body: #5a5a5a;
    --watermark: rgba(163, 23, 28, 0.05);
  }
  * { box-sizing: border-box; margin: 0; padding: 0; }
  html, body {
    width: 1200px; height: 1141px; overflow: hidden;
    background: var(--backdrop);
    font-family: 'Roboto', Arial, sans-serif;
  }
  .letterhead {
    position: absolute; left: 208px; top: 20px;
    width: 783px; height: 1100px;
    background: linear-gradient(160deg, var(--paper) 0%, var(--paper) 45%, var(--paper-shade) 100%);
    box-shadow: 0 2px 6px rgba(0,0,0,0.18);
    overflow: hidden;
  }
  .brand {
    position: absolute; left: 66px; top: 96px;
    display: flex; align-items: center; gap: 10px;
  }
  .brand-square { width: 30px; height: 30px; background: var(--brand-red); border-radius: 3px; }
  .brand-name { font-size: 26px; font-weight: 400; color: var(--brand-red); letter-spacing: 0.5px; }
  .contact {
    position: absolute; left: 534px; top: 97px;
    list-style: none; font-size: 12.2px; color: var(--ink-dark); line-height: 16.4px;
  }
  .contact li { display: flex; align-items: center; gap: 7px; }
  .contact svg { width: 10px; height: 10px; fill: var(--brand-red); flex: none; }
  .watermark {
    position: absolute; left: 236px; top: 358px; width: 306px; height: 300px;
    border: 14px solid var(--watermark); border-radius: 14px;
  }
  .letter { position: absolute; left: 70px; top: 266px; width: 644px; }
  .salutation { font-size: 18.5px; font-weight: 400; color: var(--ink-dark); margin-bottom: 27px; }
  .letter p {
    font-size: 11.2px; font-weight: 300; line-height: 16.8px; color: var(--ink-body);
    text-align: justify; margin-bottom: 16.6px;
  }
  .letter p.closing { margin-top: 33px; text-align: left; }
  .signature {
    position: absolute; left: 60px; top: 754px; width: 170px; height: 70px;
    background: linear-gradient(90deg, rgba(40,40,40,0.08), rgba(40,40,40,0.02));
    border-radius: 4px;
  }
  .address {
    position: absolute; left: 0; right: 0; top: 1053px;
    display: flex; justify-content: center; align-items: center; gap: 6px;
    font-size: 12.5px; color: var(--ink-dark);
  }
  .address svg { width: 11px; height: 14px; fill: var(--brand-red); }
</style>
</head>
<body>
<main class="letterhead">
  <header>
    <div class="brand">
      <span class="brand-square"></span>
      <span class="brand-name">Maplerise Trading</span>
    </div>
    <ul class="contact">
      <li><svg viewBox="0 0 10 10"><path d="M2 0.5 L3.6 2.6 L2.8 3.6 Q4 6 6.4 7.2 L7.4 6.4 L9.5 8 L8.4 9.5 Q3.5 9 0.5 1.6 Z"/></svg>+1 (888) 555-0142</li>
      <li><svg viewBox="0 0 10 10"><path d="M0.5 2 H9.5 V8 H0.5 Z M1.2 2.6 L5 5.4 L8.8 2.6" /></svg>sales@mapleriseinc.com</li>
      <li><svg viewBox="0 0 10 10"><circle cx="5" cy="5" r="4.6"/></svg>www.mapleriseinc.com</li>
    </ul>
  </header>

  <div class="watermark" aria-hidden="true"></div>

  <section class="letter">
    <h1 class="salutation">Dear Mr. Smith,</h1>
    <p>Lorem ipsum dolor sit amet, consectetur adipiscing elit. Donec orci purus, luctus vitae dignissim eu, iaculis sed purus. Vivamus faucibus, ipsum nec aliquet viverra, leo mauris condimentum ligula, sit amet sagittis enim ligula quis arcu. Nam egestas tortor id nisi porttitor mattis. In tortor ante, ultricies in suscipit a, tempus non massa. Vivamus et auctor mi. Fusce vel massa nulla. Phasellus nec eros mauris, et scelerisque orci.</p>
    <p>Donec malesuada orci vitae nulla accumsan porta a id massa. Quisque accumsan iaculis magna sit amet fringilla. Maecenas consequat, magna eget tincidunt semper, odio nibh rutrum mi, id feugiat ante nisi eu risus. Vestibulum nunc orci, rhoncus a placerat in, ultricies in mi. Cras mattis varius eros, vel fringilla nisi suscipit eget. Quisque scelerisque sagittis nulla at porttitor.</p>
    <p>Sed id augue vitae urna euismod commodo aliquet a quam. Pellentesque arcu velit, cursus et malesuada ut, consequat et diam. Nullam erat sem, rhoncus id ullamcorper vitae, rhoncus et arcu. In ultricies ultricies nulla, ut rutrum nisi iaculis at. Donec eu magna a metus ornare faucibus. Fusce aliquet faucibus ultricies. Morbi semper, est id tincidunt gravida, sem arcu adipiscing lacus, ac bibendum nulla leo eu purus. Quisque nec diam sed risus consectetur a ccumsan quis quis nibh. Vestibulum id purus lorem.</p>
    <p>It is a long established fact that a reader will be distracted by the readable content of a page when looking at its layout. The point of using Lorem Ipsum is that it has a more-or-less normal distribution of letters, as opposed to using 'Content here, content here', making it look like readable English. Many desktop publishing packages</p>
    <p>ada ut, consequat et diam. Nullam erat sem, rhoncus id ullamcorper vitae, rhoncus et arcu. In ultricies ultricies nulla, ut rutrum nisi iaculis at. Donec eu magna a metus ornare faucibus. Fusce aliquet faucibus ultricies. Morbi semper,</p>
    <p class="closing">Sincerely,</p>
  </section>

  <div class="signature" role="img" aria-label="Handwritten signature of the sender"></div>

  <footer class="address">
    <svg viewBox="0 0 11 14"><path d="M5.5 0 A5.5 5.5 0 0 1 11 5.5 C11 9 5.5 14 5.5 14 C5.5 14 0 9 0 5.5 A5.5 5.5 0 0 1 5.5 0 Z M5.5 3 A2.5 2.5 0 1 0 5.5 8 A2.5 2.5 0 1 0 5.5 3 Z" fill-rule="evenodd"/></svg>
    <span>48 Birchmount Ave, Suite 210, Markham</span>
  </footer>
</main>
</body>
</html>
```